Brag sheet - BRIGHTER SKIES AHEAD

DRONE INDUSTRY PROFESSIONAL
I want to take my current CV and make it pop with color and maybe add some subtle graphics - something unique.
I essentially need a 'brag sheet' to get hired as a consultant or a Senior Manager in the drone industry (working remote)
Here's the story: ‘BRIGHTER SKIES AHEAD’ is more than a byline on my website. A dear friend lost her husband to an unsafe work environment – he stepped of a roof and perished on contact. Another acquaintance ended up in a wheelchair after falling from scaffolding. Leveraging technology to save lives is a passion
PASSION
I am completely devoted to leveraging technology to save lives: My dear friend lost her husband to an unsafe work environment – he stepped of a roof and perished on contact. Another acquaintance is in a wheelchair after falling from scaffolding. Therefore, I use drone and other transformative tech in my life and in my work so that ‘BRIGHTER SKIES AHEAD’ is more than a byline on my website.
Target Market(s)
c-Level executives and professionals hiring consultants
Industry/Entity Type
drone, aerospace, search&rescue
Requirements
Must have
- pop / color
Nice to have
- subtle graphics
Should not have
- goofy clip art

```html
<!DOCTYPE html>
<html lang="en">
<head>
<meta charset="utf-8">
<title>Brag Sheet – Brighter Skies Ahead</title>
<link rel="stylesheet" href="https://fonts.googleapis.com/css2?family=Exo+2:wght@700&family=Montserrat:wght@600&family=Barlow:ital,wght@0,400;0,500;1,400&display=swap">
<style>
:root{
  --page-bg:#e7e9eb;
  --sheet:#ffffff;
  --blue:#1b8fd6;
  --blue-bright:#1fa6e0;
  --blue-dark:#1676b8;
  --panel:#eaf5fc;
  --panel-line:#bfe3f6;
  --passion:#5ec5ec;
  --ink:#2b2f33;
  --icon:#7fc6ec;
}
*{box-sizing:border-box;margin:0;padding:0}
html,body{width:1200px;height:2908px;overflow:hidden}
body{background:var(--page-bg);font-family:"Barlow",sans-serif;color:var(--ink)}
.sheet{position:absolute;left:50px;top:675px;width:1100px;height:1558px;background:var(--sheet);box-shadow:0 6px 24px rgba(0,0,0,.12);overflow:hidden}
.top-bar{position:absolute;left:0;top:0;width:100%;height:14px;background:var(--blue-bright)}
.header{position:absolute;left:19px;top:34px;width:1064px;height:244px;background:var(--panel);border:2px solid var(--panel-line);border-radius:18px}
.portrait-ring{position:absolute;left:14px;top:18px;width:208px;height:208px;border-radius:50%;background:#7dcdf0}
.portrait{position:absolute;left:14px;top:14px;width:180px;height:180px;border-radius:50%;background:radial-gradient(circle at 50% 40%,#8a8f8a,#4a5a48 60%,#2f3b33)}
.name{position:absolute;left:297px;top:68px;font-family:"Exo 2",sans-serif;font-weight:700;font-size:42px;letter-spacing:2px;color:var(--blue);white-space:nowrap}
.name-rule{position:absolute;left:297px;top:122px;width:598px;height:2px;background:var(--blue)}
.drone-art{position:absolute;left:915px;top:18px;width:160px;height:152px;border-radius:12px;background:radial-gradient(circle at 60% 40%,#2f4f8f,#6fb9e6 55%,rgba(234,245,252,0) 75%)}
.contact{position:absolute;left:305px;font-size:25px;color:#33383c;display:flex;align-items:center;gap:12px;white-space:nowrap}
.contact.address{top:140px}
.contact.lines{top:182px}
.contact svg{flex:none}
.sep{color:#9aa4ab;margin:0 14px}
.side-band,.main-band{position:absolute;height:38px;display:flex;align-items:center;font-family:"Montserrat",sans-serif;font-weight:600;font-size:24px;color:#fff;letter-spacing:.5px}
.side-band{left:0;top:342px;width:361px;background:var(--blue);padding-left:58px}
.side-band svg,.main-band svg{position:absolute;left:14px}
.main-panel{position:absolute;left:365px;top:300px;width:735px;height:1258px;background:var(--panel);border-top-left-radius:18px}
.main-band{left:365px;top:342px;width:735px;background:var(--blue-bright);padding-left:63px}
.main-band svg{left:16px}
.edu-item{position:absolute;left:57px;width:300px}
.edu-item .edu-icon{position:absolute;left:-42px;top:4px}
.edu-title{font-size:20px;font-weight:500;color:var(--blue);line-height:1.1}
.edu-text{font-size:17px;line-height:1.2;margin-top:6px}
.drone-trail{position:absolute;left:90px;top:860px;width:150px;height:647px;background:linear-gradient(180deg,rgba(31,166,224,.05),rgba(31,166,224,.35));border-radius:14px}
.job{position:absolute;left:403px;width:680px}
.job .job-icon{position:absolute;left:0;top:2px}
.job-head{padding-left:33px}
.job-title{font-size:25px;font-weight:500;color:var(--blue-bright);line-height:1.1}
.job-title b{color:var(--ink);font-size:21px;font-weight:500}
.job-role{font-size:21px;font-weight:500;line-height:1.25}
.job-tag{font-size:21px;font-style:italic;line-height:1.35;margin-top:4px}
.bullets{list-style:none;margin-top:8px;padding-left:62px}
.bullets li{position:relative;font-size:17.5px;line-height:1.22;margin-bottom:6px}
.bullets li::before{content:"";position:absolute;left:-29px;top:3px;width:13px;height:13px;border-radius:50%;border:3px solid var(--icon);box-sizing:border-box}
.passion{position:absolute;left:365px;top:1405px;width:735px;height:153px;background:var(--passion);padding:14px 30px 0 63px;color:#1f2a30}
.passion svg{position:absolute;left:18px;top:18px}
.passion h2{font-family:"Montserrat",sans-serif;font-weight:600;font-size:24px;color:#fff;letter-spacing:.5px}
.passion p{font-size:17.5px;line-height:1.2;margin-top:6px}
</style>
</head>
<body>
<main class="sheet">
  <div class="top-bar"></div>

  <header class="header">
    <div class="portrait-ring"><div class="portrait" role="img" aria-label="Portrait photo of the drone pilot holding a controller outdoors"></div></div>
    <h1 class="name">DANIEL ‘DANI’ KESSLER</h1>
    <div class="name-rule"></div>
    <div class="drone-art" role="img" aria-label="Illustration of a navy quadcopter drone with signal waves"></div>
    <div class="contact address">
      <svg width="16" height="22" viewBox="0 0 16 22"><path d="M8 0C3.6 0 0 3.5 0 7.9 0 13.8 8 22 8 22s8-8.2 8-14.1C16 3.5 12.4 0 8 0zm0 11a3 3 0 1 1 0-6 3 3 0 0 1 0 6z" fill="#1fa6e0"/></svg>
      <span>4410 Mesa Ridge Lane, Austin, TX 78745</span>
    </div>
    <div class="contact lines">
      <svg width="20" height="15" viewBox="0 0 20 15"><rect x="0" y="0" width="20" height="15" rx="1.5" fill="#1fa6e0"/><path d="M1 1l9 7 9-7" stroke="#fff" stroke-width="1.6" fill="none"/></svg>
      <span>dani@ridgelineaerial.com</span>
      <span class="sep">|</span>
      <svg width="22" height="22" viewBox="0 0 22 22"><path d="M5 2l3 4-2 2c1 2.5 3.5 5 6 6l2-2 4 3-2 3c-7 0-14-7-14-14z" fill="#1fa6e0"/><path d="M13 4a5 5 0 0 1 5 5M13 1a8 8 0 0 1 8 8" stroke="#1fa6e0" stroke-width="1.6" fill="none"/></svg>
      <span>(512) 555-0148</span>
    </div>
  </header>

  <div class="main-panel"></div>

  <h2 class="side-band">
    <svg width="32" height="26" viewBox="0 0 32 26"><path d="M16 2L1 9l15 7 15-7z" fill="none" stroke="#fff" stroke-width="2"/><path d="M7 12v7c3 3 15 3 18 0v-7" fill="none" stroke="#fff" stroke-width="2"/><path d="M29 10v8" stroke="#fff" stroke-width="2"/></svg>
    EDUCATION
  </h2>
  <h2 class="main-band">
    <svg width="32" height="26" viewBox="0 0 32 26"><rect x="2" y="7" width="28" height="17" rx="2" fill="none" stroke="#fff" stroke-width="2"/><path d="M11 7V3h10v4M2 14h28" stroke="#fff" stroke-width="2" fill="none"/></svg>
    SUMMARY OF RELEVANT EXPERIENCE
  </h2>

  <section class="edu-item" style="top:410px">
    <svg class="edu-icon" width="28" height="28" viewBox="0 0 28 28"><g stroke="#555" stroke-width="1.4" fill="none"><path d="M14 2v24M2 14h24M5 5l18 18M23 5L5 23"/><circle cx="14" cy="14" r="2"/></g></svg>
    <div class="edu-title">BFA - Architecture and Design</div>
    <div class="edu-text">Lone Star State University<br>Class of 1990</div>
  </section>

  <section class="edu-item" style="top:510px">
    <svg class="edu-icon" width="30" height="30" viewBox="0 0 30 30"><g stroke="#555" stroke-width="1.4" fill="none"><circle cx="15" cy="9" r="6"/><path d="M4 28c0-6 5-10 11-10s11 4 11 10z"/></g></svg>
    <div class="edu-title">Advanced Instruction in Business Management</div>
    <div class="edu-text">Business Analytics, Team Leadership and Project Management<br>FAA Part 107 Certification</div>
  </section>

  <section class="edu-item" style="top:640px">
    <svg class="edu-icon" width="26" height="32" viewBox="0 0 26 32"><g stroke="#555" stroke-width="1.4" fill="none"><rect x="2" y="2" width="22" height="18" rx="2"/><rect x="6" y="6" width="14" height="10"/><path d="M9 20v10h8V20"/></g></svg>
    <div class="edu-title">Advanced Certification in Thermal</div>
    <div class="edu-text">Radiometric, T&amp;D, construction, commercial and residential real estate inspection</div>
  </section>

  <div class="drone-trail" role="img" aria-label="Line illustrations of drones growing larger as they fly upward"></div>

  <article class="job" style="top:415px">
    <svg class="job-icon" width="24" height="24" viewBox="0 0 24 24"><g stroke="#777" stroke-width="1.5" fill="none"><circle cx="12" cy="12" r="10"/><circle cx="12" cy="12" r="5"/><path d="M12 0v24M0 12h24"/></g></svg>
    <div class="job-head">
      <div class="job-title">Ridgeline Aerial</div>
      <div class="job-role">(Senior Managing Director/FAA-certified sUAS Pilot)</div>
      <div class="job-tag">Full service professional drone services corporation</div>
    </div>
    <ul class="bullets">
      <li>Pilot network in-house and contract</li>
      <li>Drone program consulting and implementation for search &amp; rescue and industry customers</li>
      <li>Distinctive service with heavy lift six-rotor hose-tethered drone for liquid application and cleaning (HydraWash C-1)</li>
      <li>Expert thermal and radiometric scanning and analysis (Kestrel V2 Dual with ThermaCore)</li>
      <li>Precision solar farm and wind turbine inspections (X210 RTK and X30T, Skyrel H5e)</li>
      <li>Accurate and timely transmission and Distribution inspections (X300)</li>
      <li>Multiple successful and lucrative aerial photography missions (Falcons, Sparrows, Ravens, Swifts, Kites, Wrens, etc.)</li>
    </ul>
  </article>

  <article class="job" style="top:811px">
    <svg class="job-icon" width="24" height="24" viewBox="0 0 24 24"><g stroke="#777" stroke-width="1.5" fill="none"><circle cx="12" cy="12" r="10"/><circle cx="12" cy="12" r="5"/><path d="M12 0v24M0 12h24"/></g></svg>
    <div class="job-head">
      <div class="job-title">LedgerHaven / CoinBridge <b>(Founder)</b></div>
      <div class="job-tag">Cryptocurrency pioneer of “safe crypto trading”</div>
    </div>
    <ul class="bullets">
      <li>Established a web-based trading platform for cryptocurrency transactions with an escrow component</li>
      <li>Designed and implemented the multiple signature (multisig) transaction in OpenCoin</li>
      <li>The algorithm we crafted was incorporated into the source code of OpenCoin</li>
    </ul>
  </article>

  <article class="job" style="top:1027px">
    <svg class="job-icon" width="24" height="24" viewBox="0 0 24 24"><g stroke="#777" stroke-width="1.5" fill="none"><circle cx="12" cy="12" r="10"/><circle cx="12" cy="12" r="5"/><path d="M12 0v24M0 12h24"/></g></svg>
    <div class="job-head">
      <div class="job-title">NETWORK Payroll Systems <b>(President/CEO)</b></div>
      <div class="job-tag">Internet’s first web-based payroll processing and tax filing service</div>
    </div>
    <ul class="bullets">
      <li>Trailblazed the digital experience in an ambiguous environment</li>
      <li>Built an accurate and precise conversion program to onboard PayStream customers to our system</li>
      <li>Defined a landscape of business use cases resulting in effective marketing and explosive sales</li>
      <li>Created huge library of APIs to interface with our system</li>
      <li>Acquired by industry incumbent (PayStream)</li>
    </ul>
  </article>

  <section class="passion">
    <svg width="24" height="24" viewBox="0 0 24 24"><g stroke="#fff" stroke-width="1.6" fill="none"><rect x="8" y="8" width="8" height="8" rx="2"/><path d="M8 8L3 3M16 8l5-5M8 16l-5 5M16 16l5 5"/><circle cx="3" cy="3" r="2.5"/><circle cx="21" cy="3" r="2.5"/><circle cx="3" cy="21" r="2.5"/><circle cx="21" cy="21" r="2.5"/></g></svg>
    <h2>PASSION</h2>
    <p>‘BRIGHTER SKIES AHEAD’ is more than a byline on my website. A dear friend lost her husband to an unsafe work environment – he stepped of a roof and perished on contact. Another acquaintance ended up in a wheelchair after falling from scaffolding. Leveraging technology is a passion</p>
  </section>
</main>
</body>
</html>
```